Tellwick Asset Management - Corporate Letter Head Project

Looking for a classy design based on our current logo. Please find current logo source file in files. With our color scheme.

Target Market(s)

We're an investment firm, the letterhead needs to look professional and attractive to clients.

Industry/Entity Type

Hedgefund

Colors
0054AA
0677BA
7BADD7
CADEEF
E8F1F8

Requirements
Must have
• Our logo, address, phone number, and email

```html
<!DOCTYPE html>
<html lang="en">
<head>
<meta charset="utf-8">
<title>Tellwick Asset Management – Letterhead</title>
<link href="https://fonts.googleapis.com/css2?family=Arimo:wght@400;700&display=swap" rel="stylesheet">
<style>
  :root {
    --backdrop: #e6e6e7;
    --paper: #f1f1f2;
    --ink: #454545;
    --ink-soft: #555555;
    --brand-navy: #1b2a44;
  }
  * { margin: 0; padding: 0; box-sizing: border-box; }
  html, body { width: 1024px; height: 1200px; overflow: hidden; }
  body {
    background: var(--backdrop);
    font-family: "Arimo", Arial, sans-serif;
    color: var(--ink);
  }
  .letterhead {
    position: absolute;
    left: 102px; top: 26px;
    width: 820px; height: 1148px;
    background: var(--paper);
    box-shadow: 0 6px 28px rgba(0,0,0,0.12);
  }
  .brand {
    position: absolute;
    left: 64px; top: 48px;
    width: 160px;
    display: flex; flex-direction: column; align-items: center;
    color: var(--brand-navy);
  }
  .brand-square {
    width: 58px; height: 58px;
    border: 1.5px solid var(--brand-navy);
    margin-bottom: 14px;
  }
  .brand-name {
    font-size: 19px; font-weight: 400; line-height: 1.15;
    text-align: center; letter-spacing: 0.5px;
  }
  .contact {
    position: absolute;
    left: 595px; top: 70px;
    font-size: 12.5px; line-height: 16px; color: var(--ink-soft);
  }
  .contact-address { margin-bottom: 9px; }
  .contact-line { display: flex; align-items: center; gap: 9px; }
  .contact-line svg { width: 10px; height: 10px; fill: var(--brand-navy); flex: none; }
  .recipient {
    position: absolute;
    left: 69px; top: 326px;
    font-size: 13.5px; line-height: 15.3px;
  }
  .salutation {
    position: absolute;
    left: 70px; top: 447px;
    font-size: 15px; font-weight: 700;
  }
  .letter-body {
    position: absolute;
    left: 70px; top: 505px;
    width: 690px;
    font-size: 13.3px; line-height: 15.3px;
  }
  .letter-body p { margin-bottom: 15px; }
  .sign-off {
    position: absolute;
    left: 74px; top: 824px;
  }
  .signer-name { font-size: 17px; font-weight: 700; line-height: 21px; }
  .signer-role { font-size: 17px; line-height: 21px; }
  .signature {
    position: absolute;
    left: 69px; top: 882px;
    width: 130px; height: 66px;
    background: linear-gradient(90deg, rgba(30,30,30,0.10), rgba(30,30,30,0.04));
    border-radius: 4px;
  }
</style>
</head>
<body>
  <main class="letterhead">
    <header>
      <div class="brand">
        <div class="brand-square"></div>
        <div class="brand-name">TELLWICK ASSET<br>MANAGEMENT</div>
      </div>
      <address class="contact" style="font-style:normal">
        <div class="contact-address">412 Harbourview Road<br>Halden Bay, Canada 58120</div>
        <div class="contact-line">
          <svg viewBox="0 0 24 24" aria-hidden="true"><path d="M6.6 10.8a15.1 15.1 0 0 0 6.6 6.6l2.2-2.2c.3-.3.7-.4 1-.2 1.1.4 2.3.6 3.6.6.6 0 1 .4 1 1V20c0 .6-.4 1-1 1A17 17 0 0 1 3 4c0-.6.4-1 1-1h3.5c.6 0 1 .4 1 1 0 1.3.2 2.5.6 3.6.1.3 0 .7-.2 1z"/></svg>
          <span>604-218-5590</span>
        </div>
        <div class="contact-line">
          <svg viewBox="0 0 24 24" aria-hidden="true"><path d="M2 5h20v14H2z M2 5l10 8 10-8" /><path d="M2 5l10 8 10-8v2l-10 8L2 7z" fill="#f1f1f2"/></svg>
          <span>info@tellwick.com</span>
        </div>
      </address>
    </header>

    <section class="recipient">
      Mr Daniel Ashford<br>
      Founder and CEO<br>
      Your Company,<br>
      412 Harbourview Road, Suite 2210<br>
      Halden Bay, Canada 58120
    </section>

    <p class="salutation">Dear Sir</p>

    <section class="letter-body">
      <p>Lorem ipsum dolor sit amet. Non quam iste ut dolor repellendus aut quasi porro nam molestias ullam ut sint ipsa! Qui accusamus assumenda qui quae tempore sit quia velit aut porro tempora. Est iste explicabo aut alias impedit est sequi quis.</p>
      <p>Cum rerum molestiae id galisum odit et autem voluptas aut blanditiis iste ut aspernatur itaque ut tempora laudantium vel voluptatem repudiandae! Ea delectus omnis est voluptas odit ut assumenda quisquam eos facere sunt qui quis vitae. Qui velit dolorem in distinctio</p>
      <p>dignissimos rem voluptatem totam ut quia nostrum cum quas consequuntur. Quo aliquid earum eum optio ducimus qui fugiat veniam qui blanditiis velit ut quos dolores non officiis enim ut voluptatem veritatis.</p>
      <p>At quia sunt nam quibusdam mollitia aut rerum laudantium et inventore molestiae aut cumque consequatur. 33 minima velit rem quasi galisum ut quae magni sed praesentium possimus 33 commodi quam qui quae aperiam est enim accusantium. Sed Quis laboriosam ut suscipit maxime cum reprehenderit adipisci. Non nihil dolor ut obcaecati commodi aut Quis provident eos doloribus cumque.</p>
      <p>At quia sunt nam quibusdam mollitia aut rerum laudantium et inventore molestiae aut cumque consequatur. 33 minima velit rem quasi galisum ut quae</p>
    </section>

    <footer class="sign-off">
      <div class="signer-name">EVAN MARLOW</div>
      <div class="signer-role">President</div>
    </footer>
    <div class="signature" role="img" aria-label="Handwritten signature of the President"></div>
  </main>
</body>
</html>
```